Business Card Design for a Personal Trainer

I need a business card design for my job as a personal trainer. It should have a unique, modern and exclusive design. On the front there should be only my logo with my name and my job. 0163/2918374 Tobias Kellinger Lindenfeldweg 14 80412 Munich Germany The most important contact information is the web adress. it can be bigger than the rest, but its not necessary. The card should be 8,5cmx5,5cm big. Font: Roboto. Colors: black, white, gray, 56c1ff.

```html
<!DOCTYPE html>
<html lang="de">
<head>
<meta charset="utf-8">
<title>Tobias Kellinger – Personal Trainer Business Cards</title>
<link href="https://fonts.googleapis.com/css2?family=Roboto:wght@400;500;700&display=swap" rel="stylesheet">
<style>
  :root {
    --backdrop: #d3d4d6;
    --ink: #231f20;
    --white: #ffffff;
    --band-gray: #f0f0f2;
    --accent: #65bbe9;
    --photo-light: #8a8a8a;
    --photo-dark: #3a3a3a;
  }
  * { margin: 0; padding: 0; box-sizing: border-box; }
  html, body { width: 1200px; height: 993px; overflow: hidden; }
  body {
    background: var(--backdrop);
    font-family: "Roboto", sans-serif;
    position: relative;
  }
  .card {
    position: absolute;
    width: 519px;
    height: 334px;
    overflow: hidden;
    box-shadow: 0 2px 8px rgba(0,0,0,0.15);
  }
  .row-top { top: 130px; }
  .row-bottom { top: 529px; }
  .col-front { left: 65px; }
  .col-back { left: 616px; }

  /* front */
  .card-front { color: var(--white); }
  .card-front.dark { background: var(--ink); }
  .card-front.blue { background: var(--accent); }
  .brand-mark {
    position: absolute;
    left: 237px; top: 118px;
    width: 44px; height: 44px;
    background: var(--white);
  }
  .brand-name {
    position: absolute;
    left: 0; right: 0; top: 188px;
    text-align: center;
    font-size: 32px;
    font-weight: 400;
    line-height: 1;
  }
  .brand-role {
    position: absolute;
    left: 118px; right: 118px; top: 226px;
    display: flex; align-items: center; gap: 4px;
    font-size: 12px;
    letter-spacing: 4px;
    line-height: 1;
  }
  .brand-role::before, .brand-role::after {
    content: ""; flex: 1; height: 1px; background: var(--white);
  }

  /* back */
  .card-back { background: var(--white); color: var(--ink); }
  .contact-band {
    position: absolute; left: 0; right: 0; top: 137px; height: 138px;
    background: var(--band-gray);
  }
  .web-band {
    position: absolute; left: 238px; right: 0; top: 275px; bottom: 0;
    display: flex; align-items: center; padding-left: 24px;
    font-size: 15.5px; font-weight: 700; letter-spacing: 0.3px;
    color: var(--white);
  }
  .card-back.dark .web-band { background: var(--ink); }
  .card-back.blue .web-band { background: var(--accent); }
  .portrait {
    position: absolute; left: 0; top: 18px; width: 240px; bottom: 0;
    background: radial-gradient(ellipse at 50% 35%, var(--photo-light), var(--photo-dark) 75%);
    clip-path: polygon(22% 0, 78% 0, 80% 40%, 100% 55%, 100% 100%, 0 100%, 0 52%, 22% 40%);
  }
  .holder-name {
    position: absolute; left: 262px; top: 54px;
    font-size: 21.5px; font-weight: 700; letter-spacing: 0.3px; line-height: 1;
  }
  .holder-role {
    position: absolute; left: 262px; top: 78px;
    font-size: 12.5px; font-weight: 400; letter-spacing: 0.4px;
  }
  .contact-list {
    position: absolute; left: 262px; top: 162px;
    list-style: none; font-size: 15px; line-height: 23px;
  }
  .contact-list li { display: flex; align-items: flex-start; }
  .contact-list svg { width: 13px; height: 13px; margin: 5px 7px 0 0; flex: none; }
  .icon { fill: var(--ink); }
  .card-back.blue .icon { fill: var(--accent); }
  .contact-list .address { line-height: 19px; margin-top: 2px; }
  .contact-list .address svg { margin-top: 3px; }
</style>
</head>
<body>

  <section class="card card-front dark row-top col-front">
    <div class="brand-mark"></div>
    <div class="brand-name">TOBIAS KELLINGER</div>
    <div class="brand-role">PERSONAL TRAINER</div>
  </section>

  <section class="card card-back dark row-top col-back">
    <div class="contact-band"></div>
    <div class="portrait" role="img" aria-label="Black and white portrait photo of the trainer with crossed arms"></div>
    <div class="holder-name">TOBIAS KELLINGER</div>
    <div class="holder-role">PERSONAL TRAINER</div>
    <ul class="contact-list">
      <li><svg viewBox="0 0 16 16"><path class="icon" d="M1 3h14v10H1z M1 3l7 6 7-6" /></svg>t.kellinger@postfeld.de</li>
      <li><svg viewBox="0 0 16 16"><path class="icon" d="M3 1l3 0 1 4-2 1.5c1 2 2.5 3.5 4.5 4.5L11 9l4 1v3c0 1-1 2-2 2C6.5 15 1 9.5 1 3c0-1 1-2 2-2z"/></svg>0163/2918374</li>
      <li class="address"><svg viewBox="0 0 16 16"><path class="icon" fill-rule="evenodd" d="M8 0a5.5 5.5 0 0 1 5.5 5.5C13.5 10 8 16 8 16S2.5 10 2.5 5.5A5.5 5.5 0 0 1 8 0zm0 3a2.5 2.5 0 1 0 0 5 2.5 2.5 0 0 0 0-5z"/></svg><span>Lindenfeldweg 14<br>80412 München</span></li>
    </ul>
    <div class="web-band">www.TOBIASKELLINGER.de</div>
  </section>

  <section class="card card-front blue row-bottom col-front">
    <div class="brand-mark"></div>
    <div class="brand-name">TOBIAS KELLINGER</div>
    <div class="brand-role">PERSONAL TRAINER</div>
  </section>

  <section class="card card-back blue row-bottom col-back">
    <div class="contact-band"></div>
    <div class="portrait" role="img" aria-label="Black and white portrait photo of the trainer with crossed arms"></div>
    <div class="holder-name">TOBIAS KELLINGER</div>
    <div class="holder-role">PERSONAL TRAINER</div>
    <ul class="contact-list">
      <li><svg viewBox="0 0 16 16"><path class="icon" d="M1 3h14v10H1z M1 3l7 6 7-6" /></svg>t.kellinger@postfeld.de</li>
      <li><svg viewBox="0 0 16 16"><path class="icon" d="M3 1l3 0 1 4-2 1.5c1 2 2.5 3.5 4.5 4.5L11 9l4 1v3c0 1-1 2-2 2C6.5 15 1 9.5 1 3c0-1 1-2 2-2z"/></svg>0163/2918374</li>
      <li class="address"><svg viewBox="0 0 16 16"><path class="icon" fill-rule="evenodd" d="M8 0a5.5 5.5 0 0 1 5.5 5.5C13.5 10 8 16 8 16S2.5 10 2.5 5.5A5.5 5.5 0 0 1 8 0zm0 3a2.5 2.5 0 1 0 0 5 2.5 2.5 0 0 0 0-5z"/></svg><span>Lindenfeldweg 14<br>80412 München</span></li>
    </ul>
    <div class="web-band">www.TOBIASKELLINGER.de</div>
  </section>

</body>
</html>
```